Journal to help kids Grades 1-5 be more creative thinkers

This is a journal for kids grades 1 - 5 where they can write, color, draw and be creative. It is designed to accompany our children's book and after-school program called Pebble Pathfinders Club. We want children to use their imagination and sense of wonder as they color, create new ideas, write stories and learn all about the creative problems solving method. We want them to learn about how to use their feelings and help others in their community. We have based this on our ORBIT method, which helps teachers teach their curriculum by engaging kids in relevant and meaningful ways and helping children of all ages learn how to think for themselves. We are a non-profit organization, so all the sales go to a scholarship fund that helps teachers pay for coaching and professional development. This journal may be used in after school programs, at home, or in classrooms. We wanted the inside to be black and white so kids feel free to make it their own but the cover should be bright and inviting. This is written and designed by Molly Drabek and Rosa Penhallow on behalf of Lantern 3 ORBIT.

Target Market(s)

Parents, schools, after school programs

Industry/Entity Type

Education

Other font styles liked:
• Fun for kids

Requirements
Must have
• Bright fun colors, our logo, easy to read font for kids
Nice to have
• Our 6 characters - but we do have them throughout book -

```html
<!DOCTYPE html>
<html lang="en">
<head>
<meta charset="utf-8">
<title>Pebble Pathfinders Journal – Cover</title>
<link rel="stylesheet" href="https://fonts.googleapis.com/css2?family=Fredoka:wght@700&family=Permanent+Marker&display=swap">
<style>
  :root {
    --page-bg: #ffffff;
    --navy: #2c2a66;
    --burst-white: #ffffff;
    --burst-gold: #f2b526;
    --ribbon-red: #b8204a;
    --bulb-yellow: #fbe46a;
    --ray-teal: #1f7a72;
    --ray-purple: #6a3a86;
    --ray-orange: #ee7a2c;
    --ray-pink: #e2477a;
    --ray-green: #3f9a45;
    --ray-yellow: #f5c531;
    --ray-blue: #3d7fa6;
    --ray-red: #c9254f;
    --ray-mint: #6fb3b8;
    --star-gold: #f6c838;
  }
  * { box-sizing: border-box; margin: 0; padding: 0; }
  html, body {
    width: 1137px;
    height: 1200px;
    overflow: hidden;
    background: var(--page-bg);
  }
  .canvas {
    position: relative;
    width: 1137px;
    height: 1200px;
  }
  .cover {
    position: absolute;
    left: 250px;
    top: 95px;
    width: 672px;
    height: 1013px;
    overflow: hidden;
  }
  .sunburst-rays {
    position: absolute;
    inset: 0;
    background:
      repeating-conic-gradient(from 2deg at 52.5% 53%,
        transparent 0deg 6deg,
        rgba(255,255,255,0.75) 6deg 6.5deg,
        transparent 6.5deg 13deg),
      conic-gradient(from 0deg at 52.5% 53%,
        var(--ray-purple) 0deg 12deg,
        var(--ray-red) 12deg 22deg,
        var(--ray-green) 22deg 36deg,
        var(--ray-mint) 36deg 46deg,
        var(--ray-orange) 46deg 60deg,
        var(--ray-purple) 60deg 72deg,
        var(--ray-teal) 72deg 86deg,
        var(--ray-orange) 86deg 98deg,
        var(--ray-blue) 98deg 110deg,
        var(--ray-pink) 110deg 122deg,
        var(--ray-orange) 122deg 134deg,
        var(--ray-green) 134deg 148deg,
        var(--ray-teal) 148deg 160deg,
        var(--ray-yellow) 160deg 170deg,
        var(--ray-mint) 170deg 180deg,
        var(--ray-green) 180deg 192deg,
        var(--ray-pink) 192deg 204deg,
        var(--ray-yellow) 204deg 216deg,
        var(--ray-red) 216deg 228deg,
        var(--ray-teal) 228deg 240deg,
        var(--ray-pink) 240deg 252deg,
        var(--ray-orange) 252deg 264deg,
        var(--ray-green) 264deg 276deg,
        var(--ray-pink) 276deg 288deg,
        var(--ray-teal) 288deg 300deg,
        var(--ray-blue) 300deg 310deg,
        var(--ray-purple) 310deg 322deg,
        var(--ray-teal) 322deg 334deg,
        var(--ray-pink) 334deg 346deg,
        var(--ray-orange) 346deg 360deg);
  }
  .sunburst-glow {
    position: absolute;
    inset: 0;
    background: radial-gradient(circle at 52.5% 53%, rgba(255,255,255,0.35) 0%, rgba(255,255,255,0) 30%);
  }
  .art-spot {
    position: absolute;
    border-radius: 50%;
  }
  .art-spot--star {
    left: 120px; top: 220px; width: 200px; height: 190px;
    background: radial-gradient(circle, var(--star-gold) 0%, var(--star-gold) 45%, rgba(246,200,56,0) 72%);
  }
  .art-spot--banner {
    left: 410px; top: 230px; width: 190px; height: 170px;
    background: radial-gradient(circle, var(--star-gold) 0%, var(--star-gold) 42%, rgba(246,200,56,0) 70%);
  }
  .art-spot--brush {
    left: 50px; top: 790px; width: 200px; height: 150px;
    background: radial-gradient(circle, rgba(220,230,235,0.95) 0%, rgba(220,230,235,0.6) 40%, rgba(220,230,235,0) 70%);
  }
  .burst {
    position: absolute;
    inset: 0;
    width: 672px;
    height: 1013px;
  }
  .title-block {
    position: absolute;
    left: 135px;
    top: 378px;
    width: 440px;
    text-align: center;
    transform: rotate(-8deg);
  }
  .club-name {
    font-family: "Fredoka", sans-serif;
    font-weight: 700;
    color: var(--navy);
    text-transform: uppercase;
    line-height: 0.95;
    letter-spacing: 0.5px;
  }
  .club-name .line-one { display: block; font-size: 78px; }
  .club-name .line-two { display: block; font-size: 54px; }
  .club-mark {
    display: inline-block;
    width: 26px;
    height: 26px;
    border-radius: 50%;
    background: var(--bulb-yellow);
    vertical-align: top;
    margin-left: 8px;
    margin-top: 6px;
  }
  .journal-word {
    display: block;
    margin-top: 8px;
    font-family: "Permanent Marker", "Comic Sans MS", cursive;
    font-size: 64px;
    color: var(--navy);
    line-height: 1;
    letter-spacing: 1px;
    text-transform: uppercase;
  }
</style>
</head>
<body>
<main class="canvas">
  <section class="cover">
    <div class="sunburst-rays" aria-hidden="true"></div>
    <div class="sunburst-glow" aria-hidden="true"></div>
    <div class="art-spot art-spot--star" role="img" aria-label="Smiling yellow star holding paintbrushes"></div>
    <div class="art-spot art-spot--banner" role="img" aria-label="Glossy yellow star shape bursting out of the centre"></div>
    <div class="art-spot art-spot--brush" role="img" aria-label="Large paintbrush with white bristles sweeping outward"></div>
    <svg class="burst" viewBox="0 0 672 1013" aria-hidden="true">
      <polygon points="600,560 650,640 520,620 500,740 440,660 360,720 340,650 240,700 260,610 150,630 200,540 110,520 180,450 140,370 240,380 250,290 340,340 400,270 450,340 540,290 530,380 610,400 570,470 640,520"
               fill="var(--ribbon-red)"/>
      <polygon points="140,370 230,360 260,300 330,330 410,270 470,320 560,300 540,390 600,460 560,520 590,600 480,600 450,700 370,660 290,720 270,650 175,650 200,570 120,510 180,450"
               fill="var(--burst-white)" stroke="var(--burst-gold)" stroke-width="5" stroke-linejoin="round"/>
    </svg>
    <div class="title-block">
      <h1 class="club-name">
        <span class="line-one">Pebble<span class="club-mark"></span></span>
        <span class="line-two">Pathfinders</span>
      </h1>
      <span class="journal-word">Journal</span>
    </div>
  </section>
</main>
</body>
</html>
```